Mobile Repair Service on location needs a Web Design

We are starting a new mobile device repair service called Gadget Haven and our website needs a design!

Hello Designers!
First, we'd like to make clear this is more than a simple web design contest, we want the designers to create an idea. We want someone who can create the whole theme of the service's we provide. We want someone that can help design our visual branding, help us communicate a sentiment. And we are willing to pay for that.

Who are we?
Our company is based in Rotterdam, the Netherlands. We provide different services for all kinds of electronic devices. The kind of services we provide are, among other things, installations of hardware and software and the repair of broken or malfunctioning devices.
We are starting a new service that offers mobile device repairs on location, be it at the home of our customers, their office, or any other place. Just give us the address and we will come to you for the repair job. This is also our main USP. We have multiple skilled engineers who drive trough the country on a daily basis and can be on location within a working day. Repair is done immediately onsite while the customer waits. At this stage we will start with the smartphone product-group within the mobile devices. In a second phase we might also add tablets.
People don't want to be without their phone for weeks because of some parts that needed to be ordered by a repair center they had to sent their phone to. We offer a fully functional mobile repair center in the form of specially customized vans. These vans have all the tools and utilities needed by our engineers to safely repair your mobile device. Your phone is being repaired directly in front of you, the next business-day, on a location you desire.

For this new service we are creating a website called Gadget Haven. The website needs a story and matching design and this is where you come in. We are not looking for a simple template design we can get from any place. We need a story. We want you to create an idea, build a unique theme or vision that helps sell the product/service. This goes beyond the design of the website. We need the whole package, the design you are creating needs to have returning elements like icons, color use, images, maybe even characters etc. You name it! There needs to be a common thread in the design so we can reuse elements in, for example, the email templates, the work order or receipt we give to our customers (we may contact the winner of the contest to design these for us as well!).

The name 'Gadget Haven' is chosen. Haven (short for rehabilitate) has a bold and playful tone to it and the design needs to reflect the name. So we're looking for a somewhat playful and cheeky design. Definitely not too serious and definitely modern. We already got a logo that we love and that fit's this description (see attached design documents for the logo). It's bold, powerful and fun. Our web design needs to reflect this as well and has to fit in with our logo.
We would really like it if the design somehow incorporates elements that highlight our unique selling points (repairs on location, we come to you etc.). We would really like some form of story telling in the design. Think clumsy people breaking their phones. Teenagers in tears because they have no access to their friends. People nowadays have the need to always be 'connected'. What happens when your phone is broken or malfunctioning? We're handling tech, we are nerds and a little bit weird, but we're professionals and here to help you with your problem. The sentiment Wire Troop tries to communicate is something we really like. We're looking for fresh idea's, anything goes!

In an overview all Unique Selling Points of the Gadget haven service:
- Professional service on location. Don’t ship to us we will come to you!
- Clear pricing upfront. No hidden cost.
- Next business-day repair.
- Backed by a professional call center open 12 hours a day and open on a Saturday as well
- Backed by a professional repair center with more then 12 years of experience
- Repair is done by certified engineers
- 1 year warranty on the repair

The process:
The main function of our website will be for customers to make a repair request. A customer will visit our website and can make a repair request immediately by going through a 'request-order-flow'. In this flow he or she will need to fill in some forms and can select wich type/model/brand of mobile device he or she has and what parts need to be repaired. After a request is placed we will call the customer back (within an hour) for a short intake and to set a date/time and location. Our engineer will meet the customer at the specified location and will repair the device onsite in one of our mobile repair centers, which is a specialized van equipped with all the tools needed for device restorations.
So in short the steps are:
- Choose your device and repair job
- Place the order
- Get a callback within the hour
- Set date and location
- We will come to you.

Website functionality:
Our website is our main form of communication. So the sentiment we want to communicate needs be reflected in the design. We need a main/front page designed (preferably a long scrolling page design) containing:
1. Customers will be able to request a repair job directly on our website. So there will need to be a prominent button/link at the top of our main page that will bring the customer to this 'request-order-flow'. This is the main flow which needs to be full focus on the front page. All other items are secondary.
2. The general information of who we are and what we do, and why the customer should choose us. Preferably in short bullet-point type keywords/sentences with icons or other visual cues. See our unique selling points to get an idea of the information that will be displayed here.
3. There needs to be a section that will explain the process (see above) of a repair request step-by- step, again in brief short key sentences and with (custom) icons.
4. There needs to be a section that explains to the customer he/she can always contact us if they are not sure what the problem is with their device, and for this reason are not sure what repair request they should order.
5. We want to implement some functionality that display customer ratings or customer reviews. So there needs to be room for some kind of widget of plugin we're going to implement which shows these reviews.
6. A 'For business section' where we will explain all the options we provide for corporate clients.
7. Social media links.
8. There needs to be a menu with buttons that leads to the all sections described in the previous points.

For now, we need a design for our front page. In the second phase, when we have picked our winner, we may ask the winner to design the page(s) for our request workflow as well.

EDIT:
Finally, we have a very specific order in mind for the different segments of our website. We would like you to add some more segments that were not in our original brief as well:

1. Top header with order/request button. (should instantly make clear our main USP, we do repairs on location)
2. Our process
3. Our unique selling points / why choose us
4. The kind of repairs we do (broken screens, broken batteries, water damage, broken camera's, no sound etc.)
5. A 'meet our team' section, where we introduce some of our engineers
6. A 'contact us for any questions' section/
7. Testimonials/user reviews
8. A section where we show key performance indicators
9. 'For businesses' sections
10.'Subscribe for newsletter' field
11. Social media buttons

Industry/Entity Type

It Service

Number of Pages Required

1 page

Font styles to use
Sans Serif

Requirements
Must have
• a main/front page, design only
• custom icons/images for banners, adverts online and in print (high res)
Nice to have
• Storytelling in our design.
• Design that fits with our brand new logo.
• Elements like icons to have a flat design.
• Keep in mind that the website will need to be responsive when designing! (Ideally provide an example of the mobile design as well)
• Create a fun and trustworthy feeling.

```html
<!DOCTYPE html>
<html lang="en">
<head>
<meta charset="utf-8">
<title>Gadget Haven – Expert Repairs. Done Fast.</title>
<link href="https://fonts.googleapis.com/css2?family=Roboto:wght@300;400;500;700&display=swap" rel="stylesheet">
<style>
:root{
  --orange:#f26522;
  --green:#72d27f;
  --sky-top:#b9def0;
  --sky-bottom:#e4f2f8;
  --city-blue:#8fcbe4;
  --grass:#7cae3c;
  --grass-light:#9cc24a;
  --ink:#333740;
  --text:#5f6470;
  --muted:#8b909a;
  --light-bg:#f7f7f7;
  --footer:#252a36;
  --footer-bottom:#1d212b;
  --social:#1d5f9a;
  --icon-bg:#eef3f8;
  --white:#ffffff;
}
*{box-sizing:border-box;margin:0;padding:0}
html,body{width:1200px;height:3197px;overflow:hidden}
body{font-family:'Roboto',Arial,sans-serif;color:var(--text);background:var(--white);position:relative}
.section-title{position:absolute;left:0;width:1200px;text-align:center;font-weight:300;font-size:35px;color:var(--ink)}

/* header */
.site-header{position:absolute;top:0;left:0;width:1200px;height:64px;background:var(--white);z-index:2}
.brand{position:absolute;left:90px;top:14px;display:flex;align-items:center;gap:10px}
.brand-dot{width:30px;height:30px;border-radius:50%;background:var(--orange)}
.brand-name{font-weight:700;font-size:15px;line-height:16px;color:var(--ink);width:70px;text-transform:uppercase}
.main-nav{position:absolute;top:24px;left:477px;display:flex;font-size:13px;color:var(--ink)}
.main-nav a{text-decoration:none;color:inherit;margin-right:31px}
.main-nav a.active{color:var(--orange)}
.main-nav a.active::after{content:"";display:block;width:34px;height:2px;background:var(--orange);margin-top:19px}
.btn-request{position:absolute;left:984px;top:13px;width:126px;height:34px;background:var(--green);color:var(--white);font-size:11px;text-transform:uppercase;display:flex;align-items:center;justify-content:center;letter-spacing:.3px}

/* hero */
.hero{position:absolute;top:64px;left:0;width:1200px;height:546px;background:linear-gradient(var(--sky-top),var(--sky-bottom) 75%);overflow:hidden}
.hero-scene{position:absolute;left:0;bottom:0;width:1200px;height:290px;
  background:
    radial-gradient(ellipse 300px 210px at 50% 88%,rgba(74,170,214,.55),rgba(74,170,214,0) 100%),
    linear-gradient(to bottom,rgba(228,242,248,0) 0%,rgba(170,214,232,.55) 55%,var(--grass-light) 86%,var(--grass) 100%)}
.hero-title{position:absolute;top:160px;width:1200px;text-align:center;font-weight:300;font-size:37px;color:var(--ink)}
.hero-sub{position:absolute;top:208px;width:1200px;text-align:center;font-size:15px;color:var(--ink)}
.btn-orange{background:var(--orange);color:var(--white);font-size:11px;text-transform:uppercase;display:flex;align-items:center;justify-content:center}
.hero .btn-orange{position:absolute;left:518px;top:239px;width:164px;height:36px}

/* about */
.about-intro{position:absolute;top:745px;left:260px;width:680px;text-align:center;font-size:12.5px;line-height:20px}
.usp{position:absolute;width:380px}
.usp-icon{position:absolute;left:0;top:0;width:54px;height:54px;border-radius:50%;background:var(--icon-bg)}
.usp-icon svg{position:absolute;left:13px;top:13px}
.usp h3{position:absolute;left:55px;top:0;font-weight:400;font-size:15.5px;color:var(--ink);white-space:nowrap}
.usp p{position:absolute;left:55px;top:24px;width:320px;font-size:11.5px;line-height:19px;color:var(--muted)}

.social{position:absolute;left:1117px;top:942px;display:flex;flex-direction:column;gap:10px}
.social span{display:block;width:34px;height:34px;border-radius:50%;background:var(--social)}

/* business */
.business{position:absolute;top:1200px;left:0;width:1200px;height:452px;background:var(--light-bg)}
.business-visual{position:absolute;left:132px;top:72px;width:356px;height:356px;border-radius:50%;background:radial-gradient(circle at 50% 45%,#b6e0ec,#a3d6e6)}
.business h2{position:absolute;left:620px;top:115px;font-weight:300;font-size:35px;color:var(--ink)}
.business-lead{position:absolute;left:620px;top:183px;width:475px;font-size:12px;line-height:20px}
.check{position:absolute;left:620px;width:475px;padding-left:28px;font-size:12px;line-height:20px}
.check svg{position:absolute;left:0;top:2px}

/* process */
.step{position:absolute;width:180px;text-align:center;font-size:13px;line-height:18px;color:var(--ink)}
.step-icon{width:86px;height:86px;margin:0 auto 12px;border-radius:50%;background:var(--icon-bg);display:flex;align-items:center;justify-content:center}
.step-arrow{position:absolute;width:34px;height:34px;border-radius:50%;background:var(--orange);display:flex;align-items:center;justify-content:center}

/* contact band */
.contact-band{position:absolute;top:2082px;left:0;width:1200px;height:354px;background:var(--orange);color:var(--white);text-align:center}
.contact-band h2{position:absolute;top:92px;width:1200px;font-weight:300;font-size:35px}
.contact-band p{position:absolute;top:150px;left:290px;width:620px;font-size:13px;line-height:21px}
.btn-white{position:absolute;left:541px;top:215px;width:117px;height:37px;background:var(--white);color:var(--ink);font-size:11px;text-transform:uppercase;display:flex;align-items:center;justify-content:center}
.band-van{position:absolute;left:0;top:292px;width:121px;height:68px;border-radius:0 12px 12px 0;background:linear-gradient(#ffffff,#eef1f4)}

/* reviews */
.review-photo{position:absolute;width:72px;height:66px;background:linear-gradient(135deg,#c9e3ee,#7fa9c4)}
.review-name{position:absolute;font-size:12.5px;color:var(--ink)}
.review-name b{color:var(--orange);font-size:18px;margin-right:6px;vertical-align:-3px}
.review-box{position:absolute;height:88px;border:2px solid #e6e9f0;background:var(--white);padding:22px 26px;font-size:12px;line-height:20px;font-style:italic;color:var(--ink)}
.review-box::before{content:"";position:absolute;left:-12px;top:-2px;border-top:12px solid #d9d2ec;border-left:12px solid transparent}

/* footer */
.site-footer{position:absolute;top:2830px;left:0;width:1200px;height:367px;background:var(--footer);color:#dfe2e8}
.footer-brand{position:absolute;left:90px;top:48px;display:flex;align-items:center;gap:10px}
.footer-brand .brand-name{color:var(--white)}
.footer-about{position:absolute;left:90px;top:114px;width:250px;font-size:12px;line-height:21px;color:var(--white)}
.footer-contact{position:absolute;left:90px;font-size:12px;display:flex;align-items:center;gap:14px}
.footer-contact i{display:block;width:22px;height:22px;border-radius:3px;background:#3a4050}
.footer-contact.mail{color:var(--orange)}
.footer-col{position:absolute;top:80px}
.footer-col h4{font-weight:500;font-size:15.5px;color:var(--white);text-transform:uppercase;margin-bottom:16px;letter-spacing:.2px}
.footer-col li{list-style:none;font-size:11.5px;line-height:29px;color:#e3e6ec}
.footer-col li::before{content:"›";color:#7a8090;margin-right:14px}
.newsletter-input{width:206px;height:36px;background:#323846;font-size:11px;color:var(--white);padding:11px 18px;margin-top:-1px}
.newsletter-btn{width:106px;height:36px;margin-top:7px;background:var(--orange);color:var(--white);font-size:11px;text-transform:uppercase;display:flex;align-items:center;justify-content:center}
.footer-bottom{position:absolute;left:0;top:320px;width:1200px;height:47px;background:var(--footer-bottom);font-size:11.5px;color:var(--white)}
.footer-bottom .copy{position:absolute;left:90px;top:16px}
.footer-bottom .legal{position:absolute;right:90px;top:16px}
.to-top{position:absolute;left:1142px;top:298px;width:30px;height:32px;background:var(--orange);display:flex;align-items:center;justify-content:center}
</style>
</head>
<body>

<header class="site-header">
  <div class="brand"><span class="brand-dot"></span><span class="brand-name">Gadget Haven</span></div>
  <nav class="main-nav">
    <a class="active" href="#">Home</a><a href="#">Repair</a><a href="#">Locations</a><a href="#">Appointments</a><a href="#">Services</a><a href="#">Contact Us</a>
  </nav>
  <div class="btn-request">Request Order</div>
</header>

<section class="hero">
  <div class="hero-scene" role="img" aria-label="Flat illustration of a colourful city skyline on green grass, with a repair engineer walking in front, clouds in the sky and the white Gadget Haven van parked on the left"></div>
  <h1 class="hero-title">Expert Repairs. Done Fast.</h1>
  <p class="hero-sub">Fast, Affordable Tablet, Laptop, Game Console and Cell Phone Repair.</p>
  <div class="btn-orange">Book Appointment</div>
</section>

<h2 class="section-title" style="top:686px">About Us</h2>
<p class="about-intro">Our company is based in Rotterdam, the Netherlands. We provide different services for all kinds of electronic devices. The kind of services we provide are, among other things, installations of hardware and software and the repair of broken or malfunctioning devices.</p>

<div class="usp" style="left:160px;top:832px">
  <div class="usp-icon"><svg width="28" height="28" viewBox="0 0 24 24"><path d="M12 2a7 7 0 0 0-7 7c0 5 7 13 7 13s7-8 7-13a7 7 0 0 0-7-7z" fill="#f26522"/><circle cx="12" cy="9" r="2.6" fill="#fff"/></svg></div>
  <h3>Service on Location</h3><p>Professional service on location. Don't ship to us we will come to you!</p>
</div>
<div class="usp" style="left:160px;top:924px">
  <div class="usp-icon"><svg width="28" height="28" viewBox="0 0 24 24"><path d="M3 12l9-9h8v8l-9 9z" fill="#4cb89a"/><circle cx="16" cy="8" r="1.8" fill="#fff"/></svg></div>
  <h3>Clear Pricing</h3><p>Clear pricing upfront. No hidden cost.</p>
</div>
<div class="usp" style="left:160px;top:998px">
  <div class="usp-icon"><svg width="28" height="28" viewBox="0 0 24 24" fill="none" stroke="#2d7fc1" stroke-width="2"><path d="M4 8h15M15 4l4 4-4 4"/><path d="M20 16H5M9 12l-4 4 4 4"/></svg></div>
  <h3>Next Day</h3><p>Next business-day repair.</p>
</div>
<div class="usp" style="left:160px;top:1062px">
  <div class="usp-icon"><svg width="28" height="28" viewBox="0 0 24 24"><circle cx="12" cy="9" r="5" fill="#f26522"/><path d="M4 22c1-5 4-7 8-7s7 2 8 7z" fill="#2d7fc1"/></svg></div>
  <h3>Available 12 hours</h3><p>Backed by a professional call center open 12 hours a day and open on a Saturday as well</p>
</div>
<div class="usp" style="left:640px;top:836px">
  <div class="usp-icon"><svg width="28" height="28" viewBox="0 0 24 24"><rect x="4" y="4" width="3" height="16" fill="#f26522"/><rect x="10.5" y="4" width="3" height="16" fill="#4cb89a"/><rect x="17" y="4" width="3" height="16" fill="#2d7fc1"/></svg></div>
  <h3>12 Year Experience</h3><p>Backed by a professional repair center with more then 12 years of experience</p>
</div>
<div class="usp" style="left:640px;top:919px">
  <div class="usp-icon"><svg width="28" height="28" viewBox="0 0 24 24"><circle cx="12" cy="8" r="5" fill="#f5b041"/><path d="M4 22c1-5 4-7 8-7s7 2 8 7z" fill="#333740"/></svg></div>
  <h3>Certified Engineers</h3><p>Repair is done by certified engineers</p>
</div>
<div class="usp" style="left:640px;top:998px">
  <div class="usp-icon"><svg width="28" height="28" viewBox="0 0 24 24"><path d="M8 14l-3 8 4-2 2 3 1-7zM16 14l3 8-4-2-2 3-1-7z" fill="#2d7fc1"/><circle cx="12" cy="9" r="6" fill="#f26522"/></svg></div>
  <h3>Warranty</h3><p>1 year warranty on the repair</p>
</div>

<div class="social" aria-label="Social media links"><span></span><span></span><span></span><span></span></div>

<section class="business">
  <div class="business-visual" role="img" aria-label="Illustration of orange office towers with a location pin, set in a light blue circle"></div>
  <h2>For business</h2>
  <p class="business-lead">Lorem ipsum dolor sit amet, consectetuer adipiscing elit. Aenean commodo ligula eget dolor. Cum sociis natoque penatibus et magnis dis parturient montes, nascetur ridiculus mus donec quam felis ultricies nec.</p>
  <div class="check" style="top:257px"><svg width="16" height="16" viewBox="0 0 16 16"><circle cx="8" cy="8" r="8" fill="#c9c3e3"/><path d="M4.5 8.2l2.3 2.3 4.7-4.7" stroke="#fff" stroke-width="1.8" fill="none"/></svg>Pellentesque eu, pretium quis, sem. Nulla consequat massa quis enim. Donec pede justo fringilla vel aliquet nec vulputate eget, arcu.</div>
  <div class="check" style="top:310px"><svg width="16" height="16" viewBox="0 0 16 16"><circle cx="8" cy="8" r="8" fill="#c9c3e3"/><path d="M4.5 8.2l2.3 2.3 4.7-4.7" stroke="#fff" stroke-width="1.8" fill="none"/></svg>Nulla consequat massa quis enim. Donec pede justo fringilla vel aliquet nec vulputate eget, arcu.</div>
</section>

<h2 class="section-title" style="top:1730px">Our process</h2>
<div class="step" style="left:102px;top:1849px"><div class="step-icon"><svg width="44" height="44" viewBox="0 0 24 24"><rect x="7" y="2" width="10" height="20" rx="2" fill="#333740"/><rect x="8.5" y="4" width="7" height="14" fill="#6fc3e6"/></svg></div>Choose your device and<br>repair job</div>
<div class="step-arrow" style="left:275px;top:1875px"><svg width="12" height="12" viewBox="0 0 12 12"><path d="M4 2l4 4-4 4" stroke="#fff" stroke-width="2" fill="none"/></svg></div>
<div class="step" style="left:302px;top:1849px"><div class="step-icon"><svg width="44" height="44" viewBox="0 0 24 24"><rect x="6" y="2" width="12" height="20" rx="2" fill="#f26522"/><rect x="7.5" y="4" width="9" height="14" fill="#fff"/><circle cx="12" cy="11" r="2.5" fill="#f5b041"/></svg></div>Place the order</div>
<div class="step-arrow" style="left:475px;top:1875px"><svg width="12" height="12" viewBox="0 0 12 12"><path d="M4 2l4 4-4 4" stroke="#fff" stroke-width="2" fill="none"/></svg></div>
<div class="step" style="left:507px;top:1849px"><div class="step-icon"><svg width="48" height="48" viewBox="0 0 24 24"><circle cx="12" cy="12" r="10" fill="#f5a623"/><circle cx="12" cy="12" r="7.5" fill="#fff"/><path d="M12 7v5l3 2" stroke="#333740" stroke-width="1.6" fill="none"/></svg></div>Get a callback within<br>the hour</div>
<div class="step-arrow" style="left:680px;top:1875px"><svg width="12" height="12" viewBox="0 0 12 12"><path d="M4 2l4 4-4 4" stroke="#fff" stroke-width="2" fill="none"/></svg></div>
<div class="step" style="left:713px;top:1849px"><div class="step-icon"><svg width="44" height="44" viewBox="0 0 24 24"><rect x="3" y="4" width="18" height="17" rx="1" fill="#fff" stroke="#4cb89a" stroke-width="1.5"/><rect x="3" y="4" width="18" height="4" fill="#4cb89a"/><text x="12" y="18" font-size="8" text-anchor="middle" fill="#333740" font-family="Roboto,sans-serif">19</text></svg></div>Set date and location</div>
<div class="step-arrow" style="left:887px;top:1875px"><svg width="12" height="12" viewBox="0 0 12 12"><path d="M4 2l4 4-4 4" stroke="#fff" stroke-width="2" fill="none"/></svg></div>
<div class="step" style="left:918px;top:1849px"><div class="step-icon"><svg width="48" height="40" viewBox="0 0 30 20"><rect x="1" y="3" width="20" height="13" rx="2" fill="#fff" stroke="#333740"/><path d="M21 7h4l4 4v5h-8z" fill="#fff" stroke="#333740"/><circle cx="7" cy="17" r="2.3" fill="#333740"/><circle cx="24" cy="17" r="2.3" fill="#333740"/></svg></div>We will come to you</div>

<section class="contact-band">
  <h2>Contact Now</h2>
  <p>You can always contact us if you are not sure what the problem is with your device, and you are not sure what repair request you should order.</p>
  <div class="btn-white">Contact Us</div>
  <div class="band-van" role="img" aria-label="Illustration of the white repair van driving in from the left"></div>
</section>

<h2 class="section-title" style="top:2529px">Customer Review</h2>
<div class="review-photo" style="left:90px;top:2625px" role="img" aria-label="Customer portrait photo"></div>
<div class="review-name" style="left:218px;top:2617px"><b>❝</b>John Smith</div>
<div class="review-box" style="left:192px;top:2645px;width:377px">Lorem ipsum dolor sit amet, consectetuer adipiscing elit. Aenean commodo ligula eget dolor .</div>
<div class="review-photo" style="left:633px;top:2625px" role="img" aria-label="Customer portrait photo"></div>
<div class="review-name" style="left:755px;top:2617px"><b>❝</b>John Doe</div>
<div class="review-box" style="left:729px;top:2645px;width:381px">Lorem ipsum dolor sit amet, consectetuer adipiscing elit. Aenean commodo ligula eget dolor .</div>

<footer class="site-footer">
  <div class="footer-brand"><span class="brand-dot"></span><span class="brand-name">Gadget Haven</span></div>
  <p class="footer-about">Lorem ipsum dolor sit amet, consectetuer adipiscing elit aenean commodo ligula eget dolor aenean massa.</p>
  <div class="footer-contact" style="top:185px"><i></i>Call Us : +31 10 555 0142</div>
  <div class="footer-contact mail" style="top:215px"><i></i>info@gadgethaven.example</div>

  <div class="footer-col" style="left:390px"><h4>Orders &amp; Returns</h4><ul>
    <li>Order Status</li><li>Shipping, Delivery &amp; Store Pickup</li><li>Return &amp; Exchange Promise</li><li>Price Match Guarantee</li><li>Pay With Points</li><li>More Orders &amp; Returns Help</li></ul></div>
  <div class="footer-col" style="left:665px"><h4>Support &amp; Services</h4><ul>
    <li>Customer Service</li><li>Protection Plans</li><li>Schedule a Service</li><li>Trade-In Program</li><li>Product Recalls</li><li>More Support &amp; Services</li></ul></div>
  <div class="footer-col" style="left:904px"><h4>Newsletter</h4>
    <div class="newsletter-input">Email</div>
    <div class="newsletter-btn">Subscribe</div></div>

  <div class="to-top"><svg width="12" height="12" viewBox="0 0 12 12"><path d="M2 8l4-4 4 4" stroke="#fff" stroke-width="2" fill="none"/></svg></div>
  <div class="footer-bottom">
    <span class="copy">Copyright 2017 | All Right Reserved</span>
    <span class="legal">Terms &amp; Conditions &nbsp;|&nbsp; Privacy Policy</span>
  </div>
</footer>

</body>
</html>
```